A multi-page brochure that explains our firm ,KLV Wealth Management

We have a current brochure attached but it is a compilation of several items combined into one. We would like this to have the same content but be one complete theme. We are a financial planning form so it needs to have a level of professionalism but also a comfortable approach for clients and showing that was have a lot of resources and experience. We cater mostly to the 55-60+ age community.

We need the front page picture changed. lake themed would be great, like our website www.TheMostowField.com
Just to be clear we use KLV Wealth Management now as our company name. Parent company name is The Mostow Field LLC. I attached the current mock brochure and our new logos.
Our logo colors are:
KLV WM Logo Colors:

Blue:
HEX: #0f75bc
RGB: rgba(15,117,188,255)

Grey:
HEX: #6d6e71
RGB: rgba(109,110,113,255)

Target Market(s)

High-level individuals that are looking for financial guidance who are 40 years old and up

Industry/Entity Type

Wealth Management

Requirements
Must have
• Clean and crisp
Nice to have
• https://www.bramblequayfunds.com/wealth-management-brochure , this is a sample we like

```html
<!DOCTYPE html>
<html lang="en">
<head>
<meta charset="utf-8">
<title>KLV Wealth Management — Brochure Spreads</title>
<link href="https://fonts.googleapis.com/css2?family=Inter:wght@400;500;600;700&display=swap" rel="stylesheet">
<style>
  :root{
    --blue:#0f75bc;
    --blue-dark:#0b4f8a;
    --navy:#0a3a6b;
    --grey:#6d6e71;
    --charcoal:#3a3b3e;
    --ink:#222428;
    --rule:#e3e7ec;
    --ring:#d6e6f4;
    --canvas:#f1f0ee;
  }
  *{box-sizing:border-box;margin:0;padding:0}
  html,body{width:1028px;height:1200px;overflow:hidden}
  body{background:var(--canvas);font-family:"Inter",Arial,sans-serif;color:var(--ink);position:relative}
  .spread{position:absolute;left:157px;width:714px;height:508px;display:flex;box-shadow:0 10px 28px rgba(0,0,0,.16)}
  .spread--firm{top:62px}
  .spread--wealth{top:626px}
  .page{position:relative;width:357px;height:508px;background:#fff;overflow:hidden}
  .page--left{box-shadow:inset -10px 0 14px -10px rgba(0,0,0,.18)}
  .page--right{box-shadow:inset 10px 0 14px -10px rgba(0,0,0,.14)}
  .abs{position:absolute}

  .runner{position:absolute;top:16px;left:18px;display:flex;align-items:center;gap:5px;font-size:5.4px;color:var(--ink);z-index:3}
  .runner::before{content:"";width:4px;height:4px;background:var(--ink)}
  .runner::after{content:"";width:110px;height:1px;background:var(--blue);margin-left:5px}
  .runner--light{color:#fff}
  .runner--light::before{background:#fff}
  .runner--light::after{background:#fff}
  .swoosh{position:absolute;top:0;right:0;width:160px;height:46px;z-index:2}

  .title{position:absolute;left:18px;line-height:1.05}
  .title strong{display:block;color:var(--blue);font-size:15.5px;font-weight:700}
  .title span{display:block;font-size:15px;font-weight:400;color:var(--ink)}
  .title--inline strong,.title--inline span{display:inline}
  .copy{font-size:7.2px;line-height:1.55;color:#33363a}
  .heading{color:var(--blue);font-size:9.6px;font-weight:700}

  .photo{position:absolute}

  .principle{position:absolute;left:16px;width:226px;border:1px solid var(--rule);background:#fafbfc;padding:7px 9px}
  .principle h3{font-size:7.6px;font-weight:600;display:flex;align-items:center;gap:5px;margin-bottom:4px}
  .principle h3 svg{width:9px;height:9px}
  .principle p{font-size:6.1px;line-height:1.55;color:#33363a}
  .principle--active{background:var(--blue);border-color:var(--blue);color:#fff}
  .principle--active p{color:#e6f1fa}
  .caption{position:absolute;font-size:6.6px;color:var(--ink);text-align:center;width:90px}

  .band{position:absolute;left:14px;width:334px;background:linear-gradient(90deg,var(--blue-dark),var(--blue));color:#fff;font-size:7.4px;line-height:1.35;padding:7px 13px}

  .item{position:absolute;display:flex;align-items:center;gap:7px;font-size:6.8px;line-height:1.3;color:var(--ink)}
  .ico{flex:none;width:15px;height:15px;border-radius:50%;background:var(--blue);box-shadow:0 0 0 2px var(--ring);display:flex;align-items:center;justify-content:center}
  .ico svg{width:8px;height:8px}

  .note{position:absolute;background:var(--navy);color:#d9e6f2;font-size:3.9px;line-height:1.45;padding:6px 10px}

  .brand{position:absolute;left:16px;bottom:34px;font-size:7.4px;font-weight:600;color:var(--blue);display:flex;align-items:center;gap:4px}
  .brand i{width:5px;height:5px;background:currentColor;display:block}
  .brand--light{color:#fff}
  .legal{position:absolute;left:16px;right:16px;bottom:14px;border-top:1px solid var(--rule);padding-top:4px;font-size:3.9px;line-height:1.45;color:#9a9ca0}
  .legal--light{color:#d9dadd;border-color:rgba(255,255,255,.5)}
</style>
</head>
<body>

<svg width="0" height="0" style="position:absolute" aria-hidden="true">
  <defs>
    <linearGradient id="swooshBlue" x1="0" y1="0" x2="1" y2="0">
      <stop offset="0" stop-color="#0b4f8a"/>
      <stop offset="1" stop-color="#1a86cf"/>
    </linearGradient>
    <symbol id="swoosh" viewBox="0 0 160 46">
      <path d="M0 0 C30 30 95 48 160 22 L160 0 Z" fill="url(#swooshBlue)"/>
      <path d="M14 0 C45 20 100 26 150 0 Z" fill="#3a3b3e"/>
    </symbol>
    <symbol id="arrows" viewBox="0 0 10 10"><path d="M2 3h6M6 1l2 2-2 2M8 7H2M4 5L2 7l2 2" stroke="#fff" stroke-width="1" fill="none"/></symbol>
    <symbol id="doc" viewBox="0 0 10 10"><rect x="2" y="2" width="6" height="6" stroke="#fff" fill="none" stroke-width="1"/><path d="M3.5 4h3M3.5 6h3" stroke="#fff" stroke-width=".8"/></symbol>
    <symbol id="coin" viewBox="0 0 10 10"><path d="M5 2a3 3 0 1 0 3 3H5z" fill="none" stroke="#fff" stroke-width="1"/></symbol>
    <symbol id="tag" viewBox="0 0 10 10"><path d="M5 1.5L8.5 5 5 8.5 1.5 5z" fill="none" stroke="#fff" stroke-width="1"/><circle cx="5" cy="5" r=".9" fill="#fff"/></symbol>
    <symbol id="send" viewBox="0 0 10 10"><path d="M1.5 5L8.5 1.5 6 8.5 5 5z" fill="none" stroke="#fff" stroke-width="1"/></symbol>
    <symbol id="case" viewBox="0 0 10 10"><rect x="1" y="3" width="8" height="5.5" fill="none" stroke="currentColor" stroke-width="1"/><path d="M3.5 3V1.8h3V3M1 5.5h8" stroke="currentColor" stroke-width="1" fill="none"/></symbol>
    <symbol id="layers" viewBox="0 0 10 10"><path d="M5 1L9 3 5 5 1 3z M1 5l4 2 4-2 M1 7l4 2 4-2" fill="none" stroke="currentColor" stroke-width=".9"/></symbol>
  </defs>
</svg>

<!-- Spread 1: Partner / Our Firm -->
<section class="spread spread--firm">
  <article class="page page--left">
    <div class="runner">Wealth Management</div>
    <svg class="swoosh"><use href="#swoosh"/></svg>
    <h2 class="title" style="top:46px"><strong>Partner</strong><span>with a Specialist</span></h2>
    <p class="copy abs" style="left:18px;top:92px;width:312px">Understanding your unique needs and vision for the future is the starting point for our relationship. Together, we’ll assess where you are financially and where you want to be. Next, we’ll create a comprehensive wealth management plan that addresses your immediate and long-term goals. What about the unpredictable? We’ll plan for the changes that may be ahead, too.</p>
    <div class="photo" role="img" aria-label="Photo of a small group of clients seated together in a bright office, listening to an advisor" style="left:0;top:200px;width:357px;height:308px;background:linear-gradient(160deg,#d9dde2 0%,#b9b3a8 45%,#6f6c6a 80%,#3f3e40 100%)"></div>
    <svg class="abs" style="left:0;top:190px" width="357" height="150" viewBox="0 0 357 150" aria-hidden="true">
      <path d="M0 0 H357 V10 C330 60 290 110 220 92 C170 80 110 40 60 40 C35 40 15 45 0 52 Z" fill="#fff"/>
      <path d="M0 52 C15 45 35 40 60 40 C110 40 170 80 220 92 C170 90 120 60 70 56 C40 54 18 60 0 66 Z" fill="#4a4b4f"/>
      <path d="M220 92 C290 110 330 60 357 10 V40 C330 100 280 125 220 92 Z" fill="url(#swooshBlue)"/>
    </svg>
    <div class="brand brand--light"><i></i>KLV Wealth Management</div>
    <p class="legal legal--light">Securities and advisory services offered through Harborline Financial Network, Member NFSA/IPC, a Registered Investment Adviser. Fixed insurance products and services offered through Ridgeway Insurance Agency or The Mostow Field.</p>
  </article>

  <article class="page page--right">
    <div class="photo" role="img" aria-label="Photo of a bright open-plan office with hanging plants" style="left:0;top:0;width:357px;height:150px;background:linear-gradient(180deg,#6f8276 0%,#aeb9b2 40%,#c9cfcf 70%,#8a9aa0 100%)"></div>
    <div class="runner runner--light">Wealth Management</div>
    <svg class="abs" style="left:0;top:60px" width="357" height="120" viewBox="0 0 357 120" aria-hidden="true">
      <path d="M0 70 C50 50 90 15 150 20 C200 24 230 60 270 78 C300 92 330 96 357 96 V120 H0 Z" fill="#fff"/>
      <path d="M230 52 C270 90 320 100 357 96 V120 C320 118 270 100 230 52 Z" fill="url(#swooshBlue)"/>
      <path d="M250 40 C280 30 320 20 357 30 V42 C320 34 280 40 250 40 Z" fill="url(#swooshBlue)"/>
    </svg>
    <h2 class="title title--inline" style="top:128px;left:15px"><strong>Our</strong> <span>Firm</span></h2>
    <p class="copy abs" style="left:16px;top:150px;width:230px">The Mostow Field LLC, established in 1987, is an independent, full-service, financial consulting firm.</p>
    <p class="copy abs" style="left:16px;top:176px;width:290px">As we search the marketplace for innovative, strategic solutions, The Mostow Field is guided by the following principles:</p>

    <div class="principle" style="top:210px;height:52px">
      <h3><svg style="color:var(--blue)"><use href="#case"/></svg>Service</h3>
      <p>We seek to anticipate your needs and exceed your expectations in every aspect of our partnership.</p>
    </div>
    <div class="principle principle--active" style="top:268px;height:62px">
      <h3><svg style="color:#fff"><use href="#layers"/></svg>Planning</h3>
      <p>We collaborate with you by listening, asking questions, educating and helping you make informed decisions to skillfully implement appropriate, effective financial strategies.</p>
    </div>
    <div class="principle" style="top:337px;height:60px">
      <h3><svg style="color:var(--blue)"><use href="#case"/></svg>Integrity</h3>
      <p>We build long-term client relationships and are proud of the integrity and sensitivity we exhibit when working with all our clients.</p>
    </div>

    <div class="photo" role="img" aria-label="Photo of a brick office building" style="left:256px;top:211px;width:86px;height:73px;background:linear-gradient(180deg,#7fa6d6 0%,#a57a5f 55%,#6c8a4f 100%)"></div>
    <p class="caption" style="left:254px;top:289px">Minneapolis Location</p>
    <div class="photo" role="img" aria-label="Photo of a glass office tower against a blue sky" style="left:256px;top:311px;width:86px;height:73px;background:linear-gradient(160deg,#2b6fc4 0%,#8db8e6 50%,#e8eef5 100%)"></div>
    <p class="caption" style="left:254px;top:390px">San Francisco Location</p>

    <p class="copy abs" style="left:16px;top:410px;width:326px;font-size:6.6px">The Mostow Field has created an environment of objectivity and independence in which to provide independent guidance and access to the widest variety of fiscal tools to support your financial goals. Our work complements the services of your existing advisors, including CPAs and attorneys.* The degree and sophistication of the plan varies according to your circumstances.</p>

    <div class="brand"><i></i>KLV Wealth Management</div>
    <p class="legal">Securities and advisory services offered through Harborline Financial Network, Member NFSA/IPC, a Registered Investment Adviser. Fixed insurance products and services offered through Ridgeway Insurance Agency or The Mostow Field.</p>
  </article>
</section>

<!-- Spread 2: Wealth Accumulation -->
<section class="spread spread--wealth">
  <article class="page page--left">
    <div class="runner">Wealth Management</div>
    <svg class="swoosh"><use href="#swoosh"/></svg>
    <h2 class="title" style="top:38px"><strong>Wealth</strong><span>Accumulation</span></h2>
    <p class="band" style="top:79px">Wealth accumulation planning addresses your investment needs, focusing on the effective allocation of your assets according to your goals and risk tolerance.</p>

    <div class="photo" role="img" aria-label="Photo of a retired couple at home, one cooking and one using a laptop" style="left:0;top:131px;width:127px;height:145px;border-bottom-right-radius:36px;background:linear-gradient(170deg,#e6e4df 0%,#b9b2a6 50%,#5e6e86 100%)"></div>
    <h3 class="heading abs" style="left:139px;top:132px">Asset Allocation</h3>
    <p class="copy abs" style="left:139px;top:147px;width:210px">Asset allocation is the process of distributing your investments across a variety of asset categories. Our goal is to create a balance of potential risk and return that meets your goals and is comfortable for you. We’ll develop integrated strategies that address:</p>
    <div class="item" style="left:140px;top:210px"><span class="ico"><svg><use href="#arrows"/></svg></span>Portfolio optimization</div>
    <div class="item" style="left:255px;top:210px"><span class="ico"><svg><use href="#doc"/></svg></span>Tax planning</div>
    <div class="item" style="left:140px;top:238px"><span class="ico"><svg><use href="#coin"/></svg></span>Risk analysis</div>
    <div class="item" style="left:255px;top:235px"><span class="ico"><svg><use href="#tag"/></svg></span>Your investment<br>policy statement</div>

    <h3 class="heading abs" style="left:16px;top:296px">Basic Needs</h3>
    <p class="copy abs" style="left:16px;top:311px;width:218px">To plan wisely, we’ll focus on your basic financial needs and create a plan to fulfill your lifestyle desires—what you seek to accomplish with your assets. We’ll discuss and evaluate your needs for:</p>
    <div class="item" style="left:17px;top:366px"><span class="ico"><svg><use href="#arrows"/></svg></span>Cash flow</div>
    <div class="item" style="left:133px;top:363px"><span class="ico"><svg><use href="#doc"/></svg></span>Homes and<br>mortgages</div>
    <div class="item" style="left:17px;top:394px"><span class="ico"><svg><use href="#coin"/></svg></span>Education funds</div>
    <div class="item" style="left:133px;top:394px"><span class="ico"><svg><use href="#coin"/></svg></span>Retirement savings</div>
    <div class="item" style="left:17px;top:421px"><span class="ico"><svg><use href="#coin"/></svg></span>Emergency funds</div>
    <div class="item" style="left:133px;top:418px"><span class="ico"><svg><use href="#doc"/></svg></span>Savings and<br>investments</div>
    <div class="item" style="left:17px;top:447px"><span class="ico"><svg><use href="#send"/></svg></span>Eldercare planning</div>

    <div class="photo" role="img" aria-label="Photo of an older couple sitting on a wooden dock by a mountain lake" style="left:243px;top:302px;width:114px;height:136px;border-top-left-radius:34px;background:linear-gradient(180deg,#b9c6cf 0%,#7c8f94 40%,#3f5a5e 70%,#6f7f83 100%)"></div>

    <div class="brand"><i></i>KLV Wealth Management</div>
    <p class="legal">Securities and advisory services offered through Harborline Financial Network, Member NFSA/IPC, a Registered Investment Adviser. Fixed insurance products and services offered through Ridgeway Insurance Agency or The Mostow Field.</p>
  </article>

  <article class="page page--right">
    <div class="runner">Wealth Management</div>
    <svg class="swoosh"><use href="#swoosh"/></svg>
    <div class="photo" role="img" aria-label="Photo of paper cut-out figures of an elderly couple standing on stacks of coins" style="left:0;top:62px;width:118px;height:182px;border-bottom-right-radius:34px;background:linear-gradient(180deg,#4d7a52 0%,#8aa88a 45%,#7b5a3c 80%,#4a3526 100%)"></div>
    <h3 class="heading abs" style="left:139px;top:64px">Alternative Investments</h3>
    <p class="copy abs" style="left:139px;top:79px;width:208px">Alternative investments have historically reacted differently to market volatility than traditional investments. This ability to provide diversification* is one reason we may consider including some of the following in your portfolio:</p>
    <div class="item" style="left:140px;top:146px"><span class="ico"><svg><use href="#arrows"/></svg></span>Commodities</div>
    <div class="item" style="left:254px;top:146px"><span class="ico"><svg><use href="#doc"/></svg></span>Private credit</div>
    <div class="item" style="left:140px;top:171px"><span class="ico"><svg><use href="#coin"/></svg></span>Hedge funds</div>
    <div class="item" style="left:254px;top:170px"><span class="ico"><svg><use href="#tag"/></svg></span>Private equity</div>
    <div class="item" style="left:140px;top:198px"><span class="ico"><svg><use href="#coin"/></svg></span>Infrastructure</div>
    <div class="item" style="left:254px;top:197px"><span class="ico"><svg><use href="#tag"/></svg></span>Real estate</div>
    <div class="item" style="left:140px;top:226px"><span class="ico"><svg><use href="#coin"/></svg></span>Oil and gas</div>

    <h3 class="heading abs" style="left:16px;top:256px">Basic Securities</h3>
    <p class="copy abs" style="left:16px;top:271px;width:212px">A key step in accumulation planning is to choose the right mix of investments, which may include the following vehicles:</p>
    <div class="item" style="left:17px;top:316px"><span class="ico"><svg><use href="#arrows"/></svg></span>Risk analysis</div>
    <div class="item" style="left:132px;top:316px"><span class="ico"><svg><use href="#doc"/></svg></span>Tax planning</div>
    <div class="item" style="left:17px;top:344px"><span class="ico"><svg><use href="#coin"/></svg></span>Portfolio optimization</div>
    <div class="item" style="left:132px;top:341px"><span class="ico"><svg><use href="#coin"/></svg></span>Your investment policy<br>statement</div>

    <div class="photo" role="img" aria-label="Photo of a smiling older couple embracing at a table with a tablet" style="left:243px;top:257px;width:114px;height:147px;border-top-left-radius:34px;border-bottom-left-radius:34px;background:linear-gradient(160deg,#c9a88a 0%,#9a7357 45%,#5a3e2d 100%)"></div>

    <p class="note" style="left:20px;top:372px;width:216px">*Diversification and asset allocation do not assure a profit or protect against a loss during a market decline. Investments are subject to risk, including the loss of principal. Some investments are not suitable for all investors, and there is no guarantee that any investing goal will be met. Alternative investments involve special risks, such as leverage, complex derivatives, adverse market forces, regulatory and tax code changes, and illiquidity. Past performance is no guarantee of future results. Talk to your financial advisor before making any investing decision.</p>

    <div class="brand"><i></i>KLV Wealth Management</div>
    <p class="legal">Securities and advisory services offered through Harborline Financial Network, Member NFSA/IPC, a Registered Investment Adviser. Fixed insurance products and services offered through Ridgeway Insurance Agency or The Mostow Field.</p>
  </article>
</section>

</body>
</html>
```